Tax Preparation flyer for LedgerWise Corp.

My Client would like a one page PDF flyer to promote upcoming tax season in Canada. This firm is affordable and all virtual. I have attached a copy of their logo and a word document with the proposed wording for the flyer. Please feel free to change if you have better suggestions.

Target Market(s)

individuals in canada

Colors
0054AA
0677BA
7BADD7
CADEEF
E8F1F8

```html
<!DOCTYPE html>
<html lang="en">
<head>
<meta charset="utf-8">
<title>LedgerWise Corp. – Tax Season Flyer</title>
<link rel="stylesheet" href="https://fonts.googleapis.com/css2?family=Lexend:wght@300;600;700&family=Nunito+Sans:wght@400;700&display=swap">
<style>
  :root {
    --blue: #1e96d6;
    --blue-deep: #0677ba;
    --cyan: #1ec0ef;
    --ink: #333436;
    --ink-soft: #2b2c2e;
    --paper: #ffffff;
    --backdrop: #e9e9e9;
  }
  * { margin: 0; padding: 0; box-sizing: border-box; }
  html, body { width: 955px; height: 1200px; overflow: hidden; background: var(--backdrop); }
  body { position: relative; font-family: "Nunito Sans", Arial, sans-serif; color: var(--ink); }

  .flyer {
    position: absolute; left: 48px; top: 53px; width: 846px; height: 1094px;
    background: var(--paper); box-shadow: 6px 6px 10px rgba(0,0,0,.25); overflow: hidden;
  }
  .hero {
    position: absolute; left: 0; top: 0; width: 846px; height: 355px;
    background: linear-gradient(100deg, #8a7a5c 0%, #cfc6b3 30%, #e9eef2 55%, #c9d4dc 75%, #f1f4f6 100%);
  }
  .hero-corner { position: absolute; left: 0; top: 0; }

  .masthead { position: absolute; left: 0; top: 355px; width: 846px; height: 108px; border-bottom: 1px solid var(--blue); }
  .brand-name {
    position: absolute; left: 75px; top: 36px;
    font-family: "Lexend", sans-serif; font-weight: 700; font-size: 38px; color: var(--blue); letter-spacing: -0.5px;
  }
  .headline {
    position: absolute; left: 520px; top: 6px;
    font-family: "Lexend", sans-serif; font-weight: 700; font-size: 60px; color: var(--blue); letter-spacing: -1px;
  }
  .tagline {
    position: absolute; left: 465px; top: 81px;
    font-family: "Lexend", sans-serif; font-weight: 600; font-size: 13.5px; color: var(--ink-soft);
  }
  .masthead-x { position: absolute; right: 0; top: 0; }

  .checklist { position: absolute; left: 52px; top: 509px; width: 360px; list-style: none; }
  .checklist li { position: relative; padding-left: 35px; font-size: 15px; line-height: 20.8px; text-align: justify; hyphens: auto; margin-bottom: 20px; }
  .checklist li svg { position: absolute; left: 0; top: 5px; }
  .accent { color: var(--blue); font-weight: 700; }

  .closing { position: absolute; left: 87px; top: 903px; font-family: "Lexend", sans-serif; }
  .closing-lead { display: block; font-weight: 600; font-size: 29px; color: var(--blue); line-height: 38px; letter-spacing: -0.3px; }
  .closing-main { display: block; font-weight: 700; font-size: 38px; color: var(--ink-soft); line-height: 46px; letter-spacing: -1px; }

  .feature { position: absolute; left: 466px; width: 331px; }
  .feature-icon { position: absolute; left: 0; top: 0; }
  .feature-body { margin-left: 54px; }
  .feature-title { font-family: "Lexend", sans-serif; font-weight: 300; font-size: 20px; color: var(--blue); line-height: 26px; }
  .feature-sub { font-family: "Lexend", sans-serif; font-weight: 600; font-size: 19px; color: var(--ink-soft); line-height: 30px; }
  .feature p { font-size: 15px; line-height: 18.4px; text-align: justify; hyphens: auto; margin-top: 4px; }
  .feature.pricing p { line-height: 20.8px; margin-top: 6px; }
  .bookkeeping { top: 503px; }
  .pricing { top: 678px; }

  .footer-band { position: absolute; left: 0; bottom: 0; width: 846px; height: 85px; background: var(--ink); }
  .footer-band svg { position: absolute; left: 0; top: 0; }
  .footer-band p {
    position: absolute; left: 87px; top: 15px; width: 710px;
    color: #fff; font-size: 14px; line-height: 18.4px; text-align: justify;
  }
  .footer-band strong { display: block; font-weight: 700; text-align: left; }
</style>
</head>
<body>
<main class="flyer">
  <div class="hero" role="img" aria-label="Photo of hands using a phone and calculator beside coin stacks and a rising arrow, next to a relaxed businessman leaning back at his desk"></div>
  <svg class="hero-corner" width="130" height="355" viewBox="0 0 130 355" aria-hidden="true">
    <polygon points="0,180 0,355 125,355" fill="var(--ink)"/>
    <polygon points="0,260 0,355 75,355" fill="var(--blue)"/>
  </svg>

  <header class="masthead">
    <div class="brand-name">LedgerWise Corp.</div>
    <h1 class="headline">Relax</h1>
    <p class="tagline">WE’VE GOT YOUR TAXES COVERED!</p>
    <svg class="masthead-x" width="126" height="108" viewBox="0 0 126 108" aria-hidden="true">
      <polygon points="126,0 126,108 110,108 60,0" fill="var(--cyan)"/>
      <polygon points="54,0 126,0 126,50" fill="var(--blue)" opacity=".6"/>
      <polygon points="0,108 60,20 80,50 30,108" fill="var(--ink)"/>
      <polygon points="40,0 66,0 126,108 98,108" fill="var(--ink)"/>
      <polygon points="66,0 80,0 126,80 126,108" fill="var(--blue)"/>
    </svg>
  </header>

  <ul class="checklist">
    <li>
      <svg width="20" height="20" viewBox="0 0 20 20" aria-hidden="true"><path d="M15 3H2v15h15v-7" fill="none" stroke="var(--ink)" stroke-width="2.2"/><path d="M6 9l4 4 9-11" fill="none" stroke="var(--ink)" stroke-width="2.2"/></svg>
      Our tax preparers have over 20 years experience and worked both in public accounting firms as well as specialized tax. Our tax services are virtual, so you don’t have to take the time for a personal visit. We take care of everything and can access all your tax slips from <span class="accent">RevCan</span> website directly into our tax software. All signing is done via SignFlow.
    </li>
    <li>
      <svg width="20" height="20" viewBox="0 0 20 20" aria-hidden="true"><path d="M15 3H2v15h15v-7" fill="none" stroke="var(--ink)" stroke-width="2.2"/><path d="M6 9l4 4 9-11" fill="none" stroke="var(--ink)" stroke-width="2.2"/></svg>
      You can fill and submit the appropriate forms, along with all your other documents, in our secure client portal. It’s important that we understand your situation and any changes in your situation from the past year.
    </li>
    <li>
      <svg width="20" height="20" viewBox="0 0 20 20" aria-hidden="true"><path d="M15 3H2v15h15v-7" fill="none" stroke="var(--ink)" stroke-width="2.2"/><path d="M6 9l4 4 9-11" fill="none" stroke="var(--ink)" stroke-width="2.2"/></svg>
      If you have a complex tax situation and would like to discuss it, we can meet invirtually over MeetSpace or TalkRoom
    </li>
  </ul>

  <h2 class="closing">
    <span class="closing-lead">Today so you can start</span>
    <span class="closing-main">TO BREATHE EASY.</span>
  </h2>

  <section class="feature bookkeeping">
    <svg class="feature-icon" width="38" height="43" viewBox="0 0 38 43" aria-hidden="true">
      <path d="M0 12a12 12 0 0 1 12-12h14a12 12 0 0 1 12 12v31H0z" fill="var(--blue)"/>
      <rect x="11" y="11" width="14" height="20" fill="none" stroke="#fff" stroke-width="1.5"/>
      <path d="M14 16h8M14 20h8M14 24h5" stroke="#fff" stroke-width="1.3"/>
      <rect x="22" y="25" width="7" height="9" fill="var(--blue)" stroke="#fff" stroke-width="1.3"/>
      <path d="M9 33v-5M12 33v-3" stroke="#fff" stroke-width="1.5"/>
    </svg>
    <div class="feature-body">
      <h3 class="feature-title">Imagine having your</h3>
      <h4 class="feature-sub">Bookkeeping on auto pilot</h4>
      <p>with everything always up to date and available at your fingertips. Anytime Anywhere You’ll always know exactly where you stand with your cash flow—how much you have, owe, are owed, and have made.</p>
    </div>
  </section>

  <section class="feature pricing">
    <svg class="feature-icon" width="38" height="43" viewBox="0 0 38 43" aria-hidden="true">
      <path d="M0 12a12 12 0 0 1 12-12h14a12 12 0 0 1 12 12v31H0z" fill="var(--blue)"/>
      <rect x="11" y="11" width="14" height="20" fill="none" stroke="#fff" stroke-width="1.5"/>
      <path d="M14 16h8M14 20h8M14 24h5" stroke="#fff" stroke-width="1.3"/>
      <rect x="22" y="25" width="7" height="9" fill="var(--blue)" stroke="#fff" stroke-width="1.3"/>
      <path d="M9 33v-5M12 33v-3" stroke="#fff" stroke-width="1.5"/>
    </svg>
    <div class="feature-body">
      <h3 class="feature-title">Pricing</h3>
      <p>Personal Tax Return $100.00 Add a business or rental schedule $125 per business or rental property. More complex tax returns will be assessed based on the complexity of the return and you will be advised before we start. Did you fall behind in filing your income tax save 20% when you file 3 or more years with us. We can do back to 2012 for filing of tax returns. If you expect a refund, the earlier you file the sooner you will receive your refund. Our average turn around time prior to April is a couple of days.</p>
    </div>
  </section>

  <footer class="footer-band">
    <svg width="90" height="85" viewBox="0 0 90 85" aria-hidden="true">
      <polygon points="0,0 30,0 70,85 0,85" fill="var(--blue)"/>
      <polygon points="30,0 40,0 73,85 63,85" fill="#fff"/>
      <polygon points="40,0 86,0 50,48" fill="var(--blue)"/>
    </svg>
    <p>How will you feel? Calm, relaxed, and able to make good business decisions. And you’ll have more time to work on your business. In short, you’ll be able to breathe easy. Sound too good to be true? <strong>That’s exactly how our clients feel once all their bookkeeping stresses are gone.</strong></p>
  </footer>
</main>
</body>
</html>
```